Consulting and solution company website in MS Webmatrix

We need a website for a new healthcare consulting company that provides management consulting and innovative solutions for patient safety. We offer 1 product with plans to add 2 more and we offer consulting services to implement, train, select, improve, the patient safety programs. We provide services to both patient safety organizations and health care provider's (mainly hospitals and health systems). We want the website to convey an innovative, hard-working, energetic company bringing new ideas to healthcare. We do not want a bunch of stock pictures of people looking smart and busy in suits and doctor/nurse garb. T We love adventure, jumping ino the middle of a problem, and are thrilled to be a small and disruptive startup. The problems are very serious and complex issues so we have to tasteful in the design but not typical and boring. he site must be in .net and be device responsive. We will manage the site in MS Webmatrix and if db is used it must be MS SQL. Many of the new and fresh templates I have seen are great. We just can't seem to pull it all together when we start "tweaking" the design. We have modified a standard template to demonstrate where we are headed, but need a higher quality than we are able to build.

My current test site is at http://sandbox.bravoridgeworks.example/

Sites I like
http://www.quillmerasoft.example/
http://fandor.velbrix.example/
https://www.taskharbor.example/
http://www.dealgrovehub.example/
http://www.wmrtq.example/

Companies in my market:
www.Kvboutcomes.example
www.Tundelcrew.example
www.Pxfixworks.example
www.Velimark.example

Target Market(s)

Healthcare providers like chief executives of hospitals, Nursing administrators, Patient Safety Professionals (www.gdwk.example) and physicians/Chief Medical Officers.

Industry/Entity Type

Management Consulting

Font styles to use
Sans Serif

Requirements
Must have
• Must have a put together feel graphically, clean, simple
Must be able to own all design materials.
Must be able to update content with some homework by us
Must have a picture slider
Must be based on .net/mssql.
Nice to have
• Blog page behind a registration process
Register and pull down whitepaper materials
Responsive design

```html
<!DOCTYPE html>
<html lang="en">
<head>
<meta charset="utf-8">
<title>BravoRidge — Patient Safety Consulting</title>
<link rel="stylesheet" href="https://fonts.googleapis.com/css2?family=Open+Sans:wght@300;400;600;700;800&display=swap">
<style>
:root{
  --blue:#2f58a8;
  --blue-dark:#2a4d95;
  --blue-soft:#8fa4d4;
  --blue-btn:#9aaad6;
  --ink:#222;
  --grey-bg:#ededed;
  --white:#fff;
}
*{margin:0;padding:0;box-sizing:border-box}
html,body{width:675px;height:1200px;overflow:hidden;background:var(--white)}
body{font-family:'Open Sans',sans-serif;color:var(--ink);position:relative}
.abs{position:absolute}

/* top bar */
.topbar{left:0;top:0;width:675px;height:23px;background:var(--blue)}
.topbar .links{left:87px;top:6px;font-size:6.5px;color:var(--white)}
.topbar .social{left:154px;top:6px;display:flex;gap:4px}
.topbar .social span{width:10px;height:10px;border-radius:50%;background:var(--white)}
.topbar .phone{left:456px;top:5px;font-size:7.5px;color:var(--white);display:flex;align-items:center;gap:3px}
.topbar .login{left:523px;top:5px;width:60px;height:14px;border-radius:4px;background:var(--white);color:var(--ink);font-size:5.2px;font-weight:600;text-align:center;line-height:14px}

/* nav */
.nav{left:0;top:23px;width:675px;height:34px;display:flex;align-items:center;padding-left:70px;font-size:8.6px;color:#777;letter-spacing:.4px}
.nav .sep{margin:0 11px;color:#999}
.nav .home{margin-right:18px}

/* hero */
.hero{left:0;top:57px;width:675px;height:241px;overflow:hidden;background:linear-gradient(90deg,#d9d2cb 0%,#ece7e2 25%,#c9aa95 40%,#f0ebe6 60%,#e8ddd6 80%,#ddd3cc 100%)}
.logo-disc{left:70px;top:-30px;width:172px;height:172px;border-radius:50%;background:var(--white)}
.logo{left:79px;top:68px;font-size:22px;font-weight:600;color:var(--ink);letter-spacing:-.3px}
.ribbon{left:71px;top:194px;width:233px;height:27px;background:var(--blue-soft);color:var(--white);font-weight:700;font-size:14px;letter-spacing:.6px;padding-left:48px;line-height:27px}
.ribbon .free{position:absolute;left:0;top:0;width:36px;height:27px;background:var(--blue);clip-path:polygon(0 0,80% 0,100% 50%,80% 100%,0 100%);font-size:8px;text-align:center;padding-right:6px;line-height:27px}

.signup{left:421px;top:12px;width:182px;height:218px;background:rgba(255,255,255,.45)}
.signup h2{height:24px;background:var(--blue);color:var(--white);font-size:8.5px;font-weight:700;text-align:center;line-height:24px;letter-spacing:.5px}
.signup .row{position:absolute;left:4px;width:174px;height:15px;display:flex;align-items:center;justify-content:space-between}
.signup label{font-size:5.6px;font-weight:700;color:var(--blue);letter-spacing:.4px}
.signup .field{width:101px;height:15px;background:linear-gradient(#fafafa,#ececec);border:1px solid #ddd;position:relative}
.signup .caret{position:absolute;right:4px;top:4px}
.signup .start{position:absolute;left:20px;top:194px;width:142px;height:24px;background:var(--blue);color:var(--white);font-size:8.5px;font-weight:700;text-align:center;line-height:24px}

.band{left:71px;top:298px;width:532px;height:40px;background:var(--blue);color:var(--white);font-weight:700;font-size:10.6px;text-align:center;line-height:13px;padding-top:7px;letter-spacing:.5px}

/* who we are */
.section-title{width:675px;left:0;text-align:center;font-weight:300;font-size:16px}
.who-title{top:354px;color:#444}
.who-text{left:95px;top:384px;width:500px;font-size:6.7px;line-height:12.9px;text-align:center;color:var(--ink)}
.service{width:175px;text-align:center}
.service .disc{margin:0 auto;width:86px;height:86px;border-radius:50%;background:radial-gradient(circle,#fff 40%,#f0f0f0 100%);display:flex;align-items:center;justify-content:center}
.service h3{margin-top:6px;font-weight:400;font-size:11px;color:var(--blue);white-space:nowrap}
.service p{margin:5px auto 0;width:140px;font-size:6.8px;line-height:13px}

/* video */
.video-band{left:0;top:637px;width:675px;height:260px;background:var(--grey-bg)}
.video-title{top:644px;color:var(--blue)}
.video{left:216px;top:668px;width:241px;height:150px;background:linear-gradient(100deg,#e4e9ee 0%,#c9a693 30%,#f2f4f6 45%,#dfe3e8 70%,#cfd4da 100%)}
.play{left:108px;top:64px}
.video-text{left:93px;top:829px;width:488px;font-size:5.3px;line-height:10.3px;text-align:center;color:#333}
.btn-start{left:283px;top:869px;width:108px;height:15px;background:var(--blue-btn);color:var(--white);font-size:6px;font-weight:700;letter-spacing:.4px;line-height:15px;padding-left:25px}
.btn-start svg{position:absolute;right:6px;top:3px}

/* why us */
.why-title{top:906px;color:var(--blue)}
.reason{width:120px;text-align:center}
.reason .tag{position:relative;width:88px;height:101px;margin:0 auto}
.reason .tag svg{position:absolute;left:0;top:0}
.reason .tag strong{position:absolute;left:-6px;top:42px;width:100px;font-size:14px;font-weight:800;line-height:16.5px;color:var(--blue)}
.reason hr{border:0;border-top:1px solid #6c8fc4;margin:6px 0 0}
.reason p{margin:5px auto 0;width:122px;font-size:5.8px;line-height:10.7px}

/* cta */
.cta{left:70px;top:1120px;width:533px;height:60px;background:var(--blue)}
.cta h2{text-align:center;color:var(--white);font-size:12.5px;font-weight:700;letter-spacing:.6px;margin-top:6px}
.cta .actions{position:absolute;left:14px;top:35px;display:flex;gap:12px}
.cta .action{width:118px;height:19px;background:var(--blue-btn);color:var(--white);font-size:7.4px;font-weight:700;padding-left:8px;line-height:19px;position:relative}
.cta .action svg{position:absolute;right:8px;top:4px}

.footer{left:0;top:1180px;width:675px;height:20px;background:var(--blue-dark);color:var(--white);font-size:6px;font-weight:600;text-align:center;line-height:20px}
</style>
</head>
<body>

<header class="abs topbar">
  <div class="abs links">About &nbsp;|&nbsp; Contact</div>
  <div class="abs social"><span></span><span></span><span></span></div>
  <div class="abs phone">
    <svg width="6" height="9" viewBox="0 0 6 9"><rect x=".5" y=".5" width="5" height="8" rx="1" fill="none" stroke="#fff"/><rect x="1.5" y="1.5" width="3" height="5" fill="#fff"/></svg>
    0000 123 4567
  </div>
  <div class="abs login">CUSTOMER LOGIN</div>
</header>

<nav class="abs nav">
  <svg class="home" width="10" height="9" viewBox="0 0 10 9"><path d="M5 0 10 4.5H8.5V9H6V6H4v3H1.5V4.5H0z" fill="#bbb"/></svg>
  <span>ABOUT US</span><span class="sep">|</span>
  <span>FOCUS AREA</span><span class="sep">|</span>
  <span>PRODUCTS &amp; SERVICES</span><span class="sep">|</span>
  <span>NEWS &amp; EVENTS</span><span class="sep">|</span>
  <span>RESOURCES</span><span class="sep">|</span>
  <span>CONTACT US</span>
</nav>

<section class="abs hero" role="img" aria-label="Photo of a doctor listening to a young girl's heartbeat with a stethoscope in a bright clinic">
  <div class="abs logo-disc"></div>
  <div class="abs logo">BravoRidge</div>
  <div class="abs ribbon"><span class="free">FREE</span>GET STARTED NOW</div>

  <form class="abs signup">
    <h2>FREE SIGN UP</h2>
    <div class="row" style="top:38px"><label>FULL NAME :</label><span class="field"></span></div>
    <div class="row" style="top:64px"><label>SURNAME :</label><span class="field"></span></div>
    <div class="row" style="top:89px"><label>EMAIL :</label><span class="field"></span></div>
    <div class="row" style="top:115px"><label>RE-ENTER EMAIL :</label><span class="field"></span></div>
    <div class="row" style="top:141px"><label>NEW PASSWORD :</label><span class="field"></span></div>
    <div class="row" style="top:166px"><label>BIRTH DATE :</label><span class="field"><svg class="caret" width="6" height="5" viewBox="0 0 6 5"><path d="M0 0h6L3 5z" fill="#2f58a8"/></svg></span></div>
    <div class="start">START</div>
  </form>
</section>

<div class="abs band">WE OFFER CONSULTING SERVICES TO IMPLEMENT,<br>TRAIN, SELECT, IMPROVE, THE PATIENT SAFETY PROGRAMS</div>

<h2 class="abs section-title who-title">Who We Are</h2>
<p class="abs who-text">Lorem Ipsum is simply dummy text of the printing and typesetting industry. Lorem Ipsum has been the industry's standard dummy text ever since the 1500s, when an unknown printer took a galley of type and scrambled it to make a type specimen book. It has survived not only five centuries, but also the leap nto electronic typesetting, remaining essentially unchanged. It was popularised in the 1960s with the release of Inkvale sheets containing Lorem Ipsum passages, and more recently with desktop publishing software like Pagewright Studio including versions of Lorem Ipsum.</p>

<div class="abs service" style="left:59px;top:448px">
  <div class="disc"><svg width="31" height="31" viewBox="0 0 31 31"><circle cx="15.5" cy="15.5" r="15.5" fill="#2f58a8"/><circle cx="15.5" cy="15.5" r="13" fill="none" stroke="#fff" stroke-width="1"/><path d="M9 16l4.5 4.5L22.5 11" fill="none" stroke="#fff" stroke-width="3"/></svg></div>
  <h3>Patient Safety Organization</h3>
  <p>Lorem Ipsum is simply dummy text of the printing and typesetting industry. Lorem Ipsum has been the industry's standard dummy text ever since the 1500s,</p>
</div>
<div class="abs service" style="left:249px;top:448px">
  <div class="disc"><svg width="31" height="31" viewBox="0 0 31 31"><circle cx="15.5" cy="15.5" r="15.5" fill="#2f58a8"/><circle cx="15.5" cy="15.5" r="13" fill="none" stroke="#fff" stroke-width="1"/><path d="M9 16l4.5 4.5L22.5 11" fill="none" stroke="#fff" stroke-width="3"/></svg></div>
  <h3>Risk, Quality &amp; Safety Integration</h3>
  <p>Lorem Ipsum is simply dummy text of the printing and typesetting industry. Lorem Ipsum has been the industry's standard dummy text ever since the 1500s,</p>
</div>
<div class="abs service" style="left:439px;top:448px">
  <div class="disc"><svg width="31" height="31" viewBox="0 0 31 31"><circle cx="15.5" cy="15.5" r="15.5" fill="#2f58a8"/><circle cx="15.5" cy="15.5" r="13" fill="none" stroke="#fff" stroke-width="1"/><path d="M9 16l4.5 4.5L22.5 11" fill="none" stroke="#fff" stroke-width="3"/></svg></div>
  <h3>Captive Management Services</h3>
  <p>Lorem Ipsum is simply dummy text of the printing and typesetting industry. Lorem Ipsum has been the industry's standard dummy text ever since the 1500s,</p>
</div>

<section class="abs video-band"></section>
<h2 class="abs section-title video-title">Watch a Short Video</h2>
<div class="abs video" role="img" aria-label="Video still of a smiling doctor talking with an elderly patient in a wheelchair">
  <svg class="abs play" width="32" height="22" viewBox="0 0 32 22"><rect width="32" height="22" rx="5" fill="#2f58a8"/><rect x="10" y="5" width="12" height="12" fill="none" stroke="#fff" stroke-width=".8"/><path d="M13 7.5v7l6-3.5z" fill="#fff"/></svg>
</div>
<p class="abs video-text">Lorem Ipsum is simply dummy text of the printing and typesetting industry. &nbsp;Lorem Ipsum is simply dummy text of the printing and typesetting industry. Lorem Ipsum is simply dummy text of the printing and typesetting industry. &nbsp;Lorem Ipsum is simply dummy text of the printing and typesetting industry. &nbsp;Lorem Ipsum is simply dummy text of the printing and typesetting industry. Lorem Ipsum is simply dummy text of the printing and typesetting industry. &nbsp;Lorem Ipsum is simply dummy text of the printing and typesetting industry.</p>
<div class="abs btn-start">GET STARTED
  <svg width="9" height="9" viewBox="0 0 9 9"><circle cx="4.5" cy="4.5" r="4" fill="none" stroke="#fff" stroke-width=".8"/><path d="M2.5 4.5h4M4.8 2.8l1.7 1.7-1.7 1.7" fill="none" stroke="#fff" stroke-width=".8"/></svg>
</div>

<h2 class="abs section-title why-title">Why You Choose Us?</h2>

<div class="abs reason" style="left:72px;top:931px">
  <div class="tag"><svg width="88" height="101" viewBox="0 0 88 101"><path d="M0 15h28l6-13h20l6 13h28v86H0z" fill="#e4e4e4"/><rect x="8" y="22" width="72" height="79" fill="#fff"/><circle cx="44" cy="11" r="3.5" fill="#fff"/></svg><strong>Most<br>Advanced<br>Team</strong></div>
  <hr><p>Lorem Ipsum is simply dummy text of the printing and typesetting industry. Lorem Ipsum has been the industry's standard dummy text ever since the 1500s,</p>
</div>
<div class="abs reason" style="left:208px;top:931px">
  <div class="tag"><svg width="88" height="101" viewBox="0 0 88 101"><path d="M0 15h28l6-13h20l6 13h28v86H0z" fill="#e4e4e4"/><path d="M8 22h26l10 8 10-8h26v79H8z" fill="#fff"/><circle cx="44" cy="11" r="3.5" fill="#fff"/></svg><strong style="top:44px">100%<br>Secure</strong></div>
  <hr><p>Lorem Ipsum is simply dummy text of the printing and typesetting industry. Lorem Ipsum has been the industry's standard dummy text ever since the 1500s,</p>
</div>
<div class="abs reason" style="left:344px;top:931px">
  <div class="tag"><svg width="88" height="101" viewBox="0 0 88 101"><path d="M0 15h28l6-13h20l6 13h28v86H0z" fill="#e4e4e4"/><rect x="8" y="22" width="72" height="79" fill="#fff"/><circle cx="44" cy="11" r="3.5" fill="#fff"/></svg><strong style="top:44px">No Win<br>No Fee</strong></div>
  <hr><p>Lorem Ipsum is simply dummy text of the printing and typesetting industry. Lorem Ipsum has been the industry's standard dummy text ever since the 1500s,</p>
</div>
<div class="abs reason" style="left:481px;top:931px">
  <div class="tag"><svg width="88" height="101" viewBox="0 0 88 101"><path d="M0 15h28l6-13h20l6 13h28v86H0z" fill="#e4e4e4"/><rect x="8" y="22" width="72" height="79" fill="#fff"/><circle cx="44" cy="11" r="3.5" fill="#fff"/></svg><strong style="top:38px">Save time<br>and Stress</strong></div>
  <hr><p>Lorem Ipsum is simply dummy text of the printing and typesetting industry. Lorem Ipsum has been the industry's standard dummy text ever since the 1500s,</p>
</div>

<section class="abs cta">
  <h2>DISCUSS YOUR NEEDS WITH OUR ADVANCED TEAM ANY TIME</h2>
  <div class="actions">
    <div class="action">Get Quote by Phone<svg width="7" height="11" viewBox="0 0 7 11"><rect x=".5" y=".5" width="6" height="10" rx="1" fill="none" stroke="#fff"/><rect x="1.5" y="1.8" width="4" height="6" fill="#fff"/></svg></div>
    <div class="action">Contact Us by E-Mail<svg width="14" height="10" viewBox="0 0 14 10"><rect width="14" height="10" fill="#fff"/><path d="M0 0l7 6 7-6" fill="none" stroke="#9aaad6" stroke-width="1"/></svg></div>
    <div class="action">Contact Us by Mail<svg width="13" height="11" viewBox="0 0 13 11"><rect y="3" width="9" height="8" fill="#fff"/><rect x="7" y="0" width="6" height="8" fill="none" stroke="#fff"/></svg></div>
    <div class="action">If Need Live Help<svg width="12" height="11" viewBox="0 0 12 11"><path d="M1 3c0 4 4 8 8 8l2-2-2.5-2-1.5 1C5.5 7 4 5.5 3.5 4l1-1.5L2.5 0z" fill="#fff"/></svg></div>
  </div>
</section>

<footer class="abs footer">© 2014 - BravoRidge Works LLC. All rights reserved</footer>

</body>
</html>
```